Harbor Scholar Frame

The primary goal would be to develop a new vision for the Harbor Scholar Powerpt. I am attaching an older version called HS, I would like it updated to include our colors and our models with new images that make the presentation more relevant. I am also attaching brochures around the new curriculum. The Links below will give examples to the digital lessons: https://210.quillmora.net/review/content/7c2d4a91-583b-4f7e-b2d6-a4e91c0f5b37/review and https://210.quillmora.net/review/content/9f41b6c3-27da-4e85-81c4-c6d204a8e719/review. the Harbor scholar PWRPT should include some of these images and the color palet from the company brochure which is attached.
Target Market(s)
Education
Look and feel

```html
<!DOCTYPE html>
<html lang="en">
<head>
<meta charset="utf-8">
<title>Harbor Scholar Frame — Presentation Slides</title>
<link rel="stylesheet" href="https://fonts.googleapis.com/css2?family=Inter:wght@400;500;700;800&family=Hind:wght@400;500&display=swap">
<style>
  :root {
    --orange: #ef7350;
    --orange-deep: #e8623d;
    --canvas-grey: #898989;
    --ink: #111111;
    --white: #ffffff;
    --logo-grey: #6a6a6a;
    --muted: #3a3a3a;
  }
  * { box-sizing: border-box; margin: 0; padding: 0; }
  html, body { width: 1200px; height: 3160px; overflow: hidden; }
  body {
    position: relative;
    background: var(--canvas-grey);
    font-family: "Inter", Arial, sans-serif;
    color: var(--ink);
  }
  .backdrop { position: absolute; inset: 0; width: 1200px; height: 3160px; }
  .slide {
    position: absolute;
    left: 86px;
    width: 1022px;
    height: 532px;
    background: var(--white);
    overflow: hidden;
  }
  .slide--welcome { top: 85px; }
  .slide--evolution { top: 699px; }
  .slide--lms { top: 1314px; }
  .slide--loop { top: 1929px; }
  .slide--closing { top: 2544px; left: 92px; background: #1b1512; }

  .brand {
    position: absolute;
    display: flex;
    align-items: center;
    gap: 10px;
    font-family: "Inter", Arial, sans-serif;
    font-weight: 400;
    font-size: 40px;
    letter-spacing: 0.5px;
    color: var(--logo-grey);
    line-height: 1;
    z-index: 2;
  }
  .brand__dot { width: 22px; height: 22px; border-radius: 50%; background: var(--orange); flex: none; }
  .brand--light { color: var(--white); }
  .brand--light .brand__dot { background: var(--white); }

  .photo { position: absolute; }

  /* Slide 1 */
  .welcome__brand { left: 50px; top: 40px; }
  .welcome__title {
    position: absolute; left: 49px; top: 180px; z-index: 2;
    font-size: 34px; font-weight: 700; line-height: 1.55; letter-spacing: -0.4px;
    white-space: nowrap;
  }
  .welcome__note {
    position: absolute; left: 50px; top: 296px; width: 380px; z-index: 2;
    font-size: 8.6px; line-height: 1.7; color: var(--muted);
  }
  .social { position: absolute; display: flex; gap: 6px; z-index: 2; }
  .social span {
    width: 33px; height: 33px; border-radius: 50%;
    border: 1.5px solid var(--orange); display: block;
  }
  .welcome__social { left: 51px; top: 445px; }

  /* Slide 2 */
  .evolution__panel { position: absolute; left: 0; top: 0; width: 296px; height: 532px; background: var(--orange); }
  .evolution__brand { left: 37px; top: 30px; }
  .panel-title {
    position: absolute; color: var(--white); z-index: 2;
    font-size: 37px; font-weight: 700; line-height: 1.43;
  }
  .evolution__title { left: 37px; top: 184px; }
  .milestones { position: absolute; left: 583px; top: 78px; list-style: none; }
  .milestone {
    display: flex; align-items: center; height: 40px; margin-bottom: 30.5px;
    font-size: 26px; font-weight: 700; white-space: nowrap;
  }
  .milestone small { font-size: 20px; font-weight: 400; margin-left: 8px; }
  .milestone__label--wrap { line-height: 1.65; }
  .tab { width: 56px; height: 38px; margin-right: 12px; flex: none; }
  .milestone--last { align-items: flex-start; }

  /* Slide 3 */
  .lms__brand { left: 37px; top: 30px; }
  .lms__title { position: absolute; left: 37px; top: 164px; font-size: 37px; font-weight: 700; }
  .traits { position: absolute; left: 40px; top: 234px; list-style: none; font-family: "Hind", Arial, sans-serif; }
  .trait { display: flex; align-items: center; font-size: 21.5px; height: 34px; margin-bottom: 10.5px; }
  .trait svg { width: 19px; height: 19px; margin-right: 6px; flex: none; }

  /* Slide 4 */
  .loop__brand { left: 25px; top: 30px; }
  .loop__title { left: 24px; top: 186px; }
  .loop__list { position: absolute; left: 558px; top: 153px; list-style: none; }
  .loop__item { display: flex; align-items: center; height: 40px; margin-bottom: 23.5px; font-size: 26px; font-weight: 700; }

  /* Slide 5 */
  .closing__url { position: absolute; left: 0; width: 100%; top: 120px; text-align: center; color: var(--white); font-size: 20px; }
  .closing__brand { left: 50%; transform: translateX(-50%); top: 192px; font-size: 70px; gap: 18px; color: #8a8480; }
  .closing__brand .brand__dot { width: 40px; height: 40px; }
  .closing__title { position: absolute; left: 0; width: 100%; top: 296px; text-align: center; color: var(--white); font-size: 43px; font-weight: 800; letter-spacing: 1px; }
  .closing__social { left: 50%; transform: translateX(-50%); top: 398px; }
</style>
</head>
<body>

<svg class="backdrop" viewBox="0 0 1200 3160" aria-hidden="true">
  <path fill="#ef7350" d="M0 0 H1073 C1040 120 1060 200 1108 230 L1108 85 H86 V575 C50 560 20 545 0 530 Z"/>
  <path fill="#ef7350" d="M300 617 C420 655 560 650 640 617 Z"/>
  <path fill="#ef7350" d="M770 2544 C880 2505 1050 2490 1200 2505 V3160 H1114 V2544 Z"/>
  <path fill="#ef7350" d="M0 3077 H190 C175 3100 165 3130 158 3160 H0 Z"/>
  <path fill="#ef7350" d="M158 3160 C165 3130 175 3100 190 3077 H1114 V3160 Z"/>
</svg>

<!-- Slide 1: Welcome -->
<section class="slide slide--welcome">
  <svg class="photo" style="left:0;top:0" width="1022" height="532" viewBox="0 0 1022 532" role="img" aria-label="Graduation cap with golden tassel in soft light, shown through triangle frames">
    <defs>
      <linearGradient id="welcomeDark" x1="0" x2="1">
        <stop offset="0" stop-color="#1a1a1a"/><stop offset="1" stop-color="#7a3a22"/>
      </linearGradient>
      <linearGradient id="welcomeLight" x1="0" y1="0" x2="1" y2="1">
        <stop offset="0" stop-color="#e7e2ea"/><stop offset="0.55" stop-color="#d9c38a"/><stop offset="1" stop-color="#c8892e"/>
      </linearGradient>
    </defs>
    <polygon points="550,267 742,160 742,375" fill="url(#welcomeDark)" stroke="url(#welcomeDark)" stroke-width="22" stroke-linejoin="round"/>
    <polygon points="790,160 790,375 984,267" fill="url(#welcomeLight)" stroke="url(#welcomeLight)" stroke-width="22" stroke-linejoin="round"/>
    <polygon points="812,110 1022,20 1022,150" fill="url(#welcomeLight)"/>
    <polygon points="812,410 1022,300 1022,532 960,532" fill="url(#welcomeLight)"/>
  </svg>
  <div class="brand welcome__brand"><span class="brand__dot"></span>Keystep Ed</div>
  <h1 class="welcome__title">Welcome To Career Readiness<br>For All Students</h1>
  <p class="welcome__note">At the same time, the K7Q Harbor Scholar Platform deploys a social constructivist pedagogy and provides tools and content to build on that approach.</p>
  <div class="social welcome__social"><span></span><span></span><span></span><span></span></div>
</section>

<!-- Slide 2: Evolution -->
<section class="slide slide--evolution">
  <div class="evolution__panel"></div>
  <div class="brand brand--light evolution__brand"><span class="brand__dot"></span>Keystep Ed</div>
  <h2 class="panel-title evolution__title">Evolution of<br>Digital<br>Instructional<br>Tools</h2>
  <svg class="photo" style="left:296px;top:0" width="294" height="532" role="img" aria-label="Students smiling while studying together at a classroom table">
    <defs><linearGradient id="studentsGrad" x1="0" y1="0" x2="0" y2="1">
      <stop offset="0" stop-color="#6b6459"/><stop offset="0.5" stop-color="#4d5a78"/><stop offset="1" stop-color="#2e2a26"/>
    </linearGradient></defs>
    <rect width="294" height="532" fill="url(#studentsGrad)"/>
  </svg>
  <ul class="milestones">
    <li class="milestone"><svg class="tab"><use href="#tab"/></svg>Computer Labs<small>(1985)</small></li>
    <li class="milestone"><svg class="tab"><use href="#tab"/></svg>Electronic Whiteboards<small>(2000)</small></li>
    <li class="milestone"><svg class="tab"><use href="#tab"/></svg>&nbsp;In-class Computing<small>(2010)</small></li>
    <li class="milestone"><svg class="tab"><use href="#tab"/></svg>Print&#x27F6; Digital<small>&nbsp;(2012)</small></li>
    <li class="milestone milestone--last"><svg class="tab"><use href="#tab"/></svg><span class="milestone__label--wrap">Harbor Scholar<small>(Next Gen)</small><br>&nbsp;Platforms</span></li>
  </ul>
</section>

<!-- Slide 3: Traditional LMS -->
<section class="slide slide--lms">
  <svg class="photo" style="left:0;top:0" width="1022" height="532" role="img" aria-label="Hands forming a frame against a warm sunset">
    <defs><linearGradient id="sunsetGrad" x1="0" y1="0" x2="1" y2="1">
      <stop offset="0" stop-color="#c49a8a"/><stop offset="0.45" stop-color="#f2d9a8"/><stop offset="0.7" stop-color="#f4c16b"/><stop offset="1" stop-color="#8a5a48"/>
    </linearGradient></defs>
    <polygon points="356,0 1022,0 1022,532 726,532" fill="url(#sunsetGrad)"/>
  </svg>
  <div class="brand lms__brand"><span class="brand__dot"></span>Keystep Ed</div>
  <h2 class="lms__title">Traditional LMS</h2>
  <ul class="traits">
    <li class="trait"><svg><use href="#backMark"/></svg>“Teacher Proof” Technology</li>
    <li class="trait"><svg><use href="#backMark"/></svg>Closed Curriculum</li>
    <li class="trait"><svg><use href="#backMark"/></svg>Fixed Map from Assessment to Curriculum</li>
    <li class="trait"><svg><use href="#backMark"/></svg>Lab or Back of the Room</li>
    <li class="trait"><svg><use href="#backMark"/></svg>One student only</li>
  </ul>
</section>

<!-- Slide 4: Instructional Loop -->
<section class="slide slide--loop">
  <svg class="photo" style="left:0;top:0" width="558" height="532" role="img" aria-label="Smiling teacher holding a tablet in a classroom">
    <defs><linearGradient id="teacherGrad" x1="0" y1="0" x2="1" y2="1">
      <stop offset="0" stop-color="#5d6575"/><stop offset="0.5" stop-color="#3a3331"/><stop offset="1" stop-color="#6e5a66"/>
    </linearGradient></defs>
    <rect width="558" height="532" rx="22" fill="url(#teacherGrad)"/>
    <rect width="40" height="532" fill="url(#teacherGrad)"/>
  </svg>
  <div class="brand brand--light loop__brand"><span class="brand__dot"></span>Keystep Ed</div>
  <h2 class="panel-title loop__title">Traditional<br>LMS<br>Instructional<br>Loop</h2>
  <ul class="loop__list">
    <li class="loop__item"><svg class="tab"><use href="#tab"/></svg>Content Management</li>
    <li class="loop__item"><svg class="tab"><use href="#tab"/></svg>Assessment</li>
    <li class="loop__item"><svg class="tab"><use href="#tab"/></svg>Grade Book</li>
    <li class="loop__item"><svg class="tab"><use href="#tab"/></svg>SIS</li>
  </ul>
</section>

<!-- Slide 5: Closing -->
<section class="slide slide--closing">
  <svg class="photo" style="left:0;top:0" width="1022" height="532" role="img" aria-label="Dim scene of a student on a video lesson at a computer">
    <defs><linearGradient id="closingGrad" x1="0" y1="0" x2="1" y2="0">
      <stop offset="0" stop-color="#1a1513"/><stop offset="0.6" stop-color="#231c18"/><stop offset="0.85" stop-color="#3b3430"/><stop offset="1" stop-color="#1e1a18"/>
    </linearGradient></defs>
    <rect width="1022" height="532" fill="url(#closingGrad)"/>
  </svg>
  <p class="closing__url">www.routeahead-learning.com</p>
  <div class="brand closing__brand"><span class="brand__dot"></span>Keystep Ed</div>
  <h2 class="closing__title">THANK YOU</h2>
  <div class="social closing__social"><span></span><span></span><span></span><span></span></div>
</section>

<svg width="0" height="0" style="position:absolute" aria-hidden="true">
  <defs>
    <symbol id="tab" viewBox="0 0 56 38">
      <path d="M6 4 H44 L54 19 L44 34 H6 A4 4 0 0 1 2 30 V8 A4 4 0 0 1 6 4 Z" fill="#ef7350"/>
      <circle cx="29" cy="19" r="12" fill="#ffffff"/>
      <path d="M26 13 L32 19 L26 25" fill="none" stroke="#ef7350" stroke-width="3.2" stroke-linecap="round" stroke-linejoin="round"/>
    </symbol>
    <symbol id="backMark" viewBox="0 0 20 20">
      <circle cx="10" cy="10" r="9.5" fill="#ef7350"/>
      <path d="M12 5.5 L7.5 10 L12 14.5" fill="none" stroke="#ffffff" stroke-width="2.4" stroke-linecap="round" stroke-linejoin="round"/>
    </symbol>
  </defs>
</svg>

</body>
</html>
```